Recruitment website for new startup company - Calder Ashby Recruitment

Hi , I need to design a web page for my new recruitment company with the ability to link to social media accounts. The ability to add and remove job posts along with a blog page which I can update. More importantly I need the website to have the functionality of applicants being able to upload their cv and somewhere for me to store it. I will need assistance/recommendation for email address with company name, hosting and security. An about us page. The website will also need a search function for applicants to narrow down the search. Again I will need to be able to update this myself as the company grows. I have my logo ready domain address ready and would like the web site done ASAP. Thank you for your help.
Updates

Reason: Want to get a few more ideas and variations to designs done. But using logo as inspiration Thanks

Target Market(s)

Financial and property industry so professionals. New starters to senior management age range 25-60

Industry/Entity Type

Financial

Coding

Coded - Design and coding required

Number of Pages Required

4 page

Colors

Designer to choose colors to be used in the design.

Requirements
Must have
• Ability for me to add amend and remove job posts, ability for applicants to upload cv and for me to store and access it. Link to social media accounts
Should not have
• Needs to be clean approachable so not to childish but must come across as approachable and trustworthy.
• No yellow please my logo has a gold V not yellow. If it looks yellow use a different colour please. Thanks

```html
<!DOCTYPE html>
<html lang="en">
<head>
<meta charset="utf-8">
<title>Calder Ashby Recruitment</title>
<link href="https://fonts.googleapis.com/css2?family=Cinzel:wght@400;600;700&family=Open+Sans:wght@400;600;700&display=swap" rel="stylesheet">
<style>
:root{
  --navy:#1d3461;
  --navy-panel:rgba(27,42,78,.9);
  --gold:#c6a13f;
  --ink:#333;
  --muted:#555;
  --line:#d6d6d6;
  --panel:#f4f4f4;
  --row:#f1f1f1;
  --btn-grey:#e0e0e0;
  --white:#fff;
}
*{box-sizing:border-box;margin:0;padding:0}
html,body{width:748px;height:1200px;overflow:hidden;background:var(--white)}
body{position:relative;font-family:"Open Sans",sans-serif;color:var(--ink)}
.abs{position:absolute}

/* header */
.brand{left:53px;top:14px;color:var(--navy);font-family:"Cinzel",serif;line-height:1}
.brand .name{font-size:20px;font-weight:600;letter-spacing:.4px}
.brand .sub{font-size:11px;letter-spacing:3px;margin-top:6px;color:#444}
.account{top:20px;left:617px;font-size:8px;color:var(--ink)}
.account span{margin:0 7px}
.nav{top:44px;left:0;font-size:9.5px;letter-spacing:.3px;color:#333}
.nav a{position:absolute;top:0;white-space:nowrap;color:inherit;text-decoration:none}
.nav .active{font-weight:600}
.nav-mark{left:382px;top:66px;width:40px;height:2px;background:var(--gold)}

/* hero */
.hero{left:0;top:69px;width:748px;height:343px;
  background:linear-gradient(120deg,#6f5138 0%,#a57a4e 20%,#c3976a 42%,#b88a5a 62%,#93694a 84%,#5e4634 100%)}
.hero-panel{left:112px;top:174px;width:489px;height:118px;background:var(--navy-panel)}
.hero-title{left:112px;top:195px;width:489px;text-align:center;color:var(--white);font-family:"Cinzel",serif;font-weight:600;font-size:18.5px;letter-spacing:.3px}
.search{left:132px;top:235px;width:448px;height:34px;display:flex;font-size:7px;font-weight:600;letter-spacing:.3px}
.search .field{background:var(--white);border-right:1px solid #ddd;display:flex;align-items:center;padding-left:11px;color:#333}
.search .f1{width:110px}.search .f2{width:107px;padding-left:17px}.search .f3{width:129px;padding-left:14px;border-right:0}
.search .caret{margin-left:4px}
.search .go{width:102px;background:var(--gold);display:flex;align-items:center;justify-content:center;font-size:10px;font-weight:600;color:var(--navy);letter-spacing:.5px}

/* steps */
.intro{left:0;top:463px;width:748px;text-align:center}
.intro h2{font-family:"Cinzel",serif;font-weight:600;font-size:18px;color:#222;letter-spacing:.3px}
.intro p{font-size:9.5px;color:#555;margin-top:8px;letter-spacing:.2px}
.steps{left:0;top:540px}
.step-label{top:647px;width:120px;text-align:center;font-size:13px;font-weight:600;color:#444;letter-spacing:.5px}

/* jobs */
.band{left:0;top:748px;width:748px;height:410px;background:var(--panel)}
.section-title{font-family:"Cinzel",serif;font-size:18.5px;color:#222;font-weight:600;letter-spacing:.3px}
.jobs{left:54px;top:834px;width:420px;height:288px;border:1px solid var(--line);background:var(--white)}
.job{position:relative;height:71.5px}
.job.alt{background:var(--row)}
.job h3{position:absolute;left:8px;top:10px;font-size:10px;font-weight:600;color:var(--navy);letter-spacing:.1px}
.job .meta{position:absolute;left:8px;font-size:8.5px;color:#333;display:flex;align-items:center;gap:4px}
.job .loc{top:29px}.job .time{top:45px;font-weight:700}
.job .pay{position:absolute;left:220px;top:20px;font-size:9.5px;line-height:16px;color:#333}
.job .pay span{display:block;color:var(--gold)}
.job .btn{position:absolute;left:295px;top:20px;width:103px;height:30px;display:flex;align-items:center;justify-content:center;font-size:9px;background:var(--btn-grey);color:#333;border-radius:1px}
.job .btn.gold{background:var(--gold);color:var(--white)}

.featured{left:502px;top:834px;width:200px;height:259px;border:1px solid var(--line);background:var(--white)}
.featured .photo{height:129px;background:linear-gradient(160deg,#8a8f88 0%,#5f625d 45%,#2d2f33 100%);position:relative}
.featured .tag{position:absolute;left:9px;top:72px;background:var(--gold);color:var(--white);font-size:8.5px;font-weight:700;padding:3px 6px;border-radius:1px}
.featured .role{position:absolute;left:11px;top:92px;color:var(--white);font-size:8.5px;font-weight:600;line-height:12px}
.featured .text{padding:14px 7px 0 8px;font-size:8.2px;line-height:12.8px;color:#444}
.featured .more{padding:6px 8px;font-size:8.5px;color:var(--navy)}

.footer{left:0;top:1172px;width:748px;text-align:center;font-size:8px;color:#444}
</style>
</head>
<body>

<header>
  <div class="abs brand"><div class="name">CALDER ASHBY</div><div class="sub">RECRUITMENT</div></div>
  <div class="abs account">Login<span>|</span>Register</div>
  <nav class="abs nav">
    <a class="active" style="left:387px">HOME</a>
    <a style="left:441px">ABOUT</a>
    <a style="left:499px">RECRUITMENT</a>
    <a style="left:590px">NEWS</a>
    <a style="left:642px">CONTACT</a>
  </nav>
  <div class="abs nav-mark"></div>
</header>

<section>
  <div class="abs hero" role="img" aria-label="Overhead photo of a team working together around a wooden desk with laptops, papers and coffee"></div>
  <div class="abs hero-panel"></div>
  <h1 class="abs hero-title">MULTI-INDUSTRY RECRUITMENT AGENCY</h1>
  <div class="abs search">
    <div class="field f1">JOB KEYWORDS</div>
    <div class="field f2">LOCATION<svg class="caret" width="7" height="5" viewBox="0 0 7 5"><path d="M1 1l2.5 2.5L6 1" fill="none" stroke="#333" stroke-width="1"/></svg></div>
    <div class="field f3">SECTOR<svg class="caret" width="7" height="5" viewBox="0 0 7 5"><path d="M1 1l2.5 2.5L6 1" fill="none" stroke="#333" stroke-width="1"/></svg></div>
    <div class="go">SEARCH</div>
  </div>
</section>

<section>
  <div class="abs intro">
    <h2>ALL THE JOBS YOU WANT IN ONE SIMPLE PLACE</h2>
    <p>FIND THE JOBS YOU IN JUST A FEW SIMPLE QUICKS.</p>
  </div>
  <svg class="abs steps" width="748" height="100" viewBox="0 540 748 100">
    <g fill="none" stroke="#aaa" stroke-width="1.2" stroke-dasharray="10 8">
      <path d="M86 622 L122 604"/>
      <path d="M198 584 Q260 568 332 585"/>
      <path d="M415 610 Q480 622 548 604"/>
      <path d="M630 578 Q648 570 660 560"/>
    </g>
    <g stroke="#aaa" stroke-width="1.4">
      <path d="M284 572v12M278 578h12"/><path d="M456 608v12M450 614h12"/>
    </g>
    <path d="M654 571l14-8-3-2 4-1 -2 3 -3-1z" fill="#999"/>
    <g fill="#d8d8d8" stroke="#eee" stroke-width="2">
      <circle cx="161" cy="596" r="38"/><circle cx="377" cy="596" r="38"/><circle cx="594" cy="596" r="38"/>
    </g>
    <g fill="none" stroke="#222" stroke-width="3.5" stroke-linecap="round">
      <circle cx="158" cy="593" r="10"/><path d="M166 601l8 8"/>
    </g>
    <g fill="none" stroke="#222" stroke-width="2.5" stroke-linejoin="round">
      <path d="M382 583h-18v26h26v-12"/>
      <path d="M374 600l2-7 14-14 5 5-14 14z" fill="#222"/>
    </g>
    <g fill="none" stroke="#222" stroke-width="2.2" stroke-linecap="round">
      <path d="M587 604c0-5-6-7-6-14a13 13 0 0 1 26 0c0 7-6 9-6 14z"/>
      <path d="M588 608h12M589 612h10M591 616h6"/>
      <path d="M594 570v-5M576 577l-4-3M612 577l4-3M570 592h-5M618 592h5"/>
    </g>
  </svg>
  <div class="abs step-label" style="left:101px">SEARCH</div>
  <div class="abs step-label" style="left:317px">APPLY</div>
  <div class="abs step-label" style="left:537px">HIRED</div>
</section>

<section>
  <div class="abs band"></div>
  <h2 class="abs section-title" style="left:53px;top:786px">RECENT JOBS</h2>
  <h2 class="abs section-title" style="left:507px;top:786px">FEATURED JOB</h2>

  <div class="abs jobs">
    <div class="job alt">
      <h3>SALES &amp; MARKETING COARDINATOR</h3>
      <div class="meta loc"><svg width="9" height="10" viewBox="0 0 9 10"><path d="M4.5 9.5S1 6 1 4a3.5 3.5 0 0 1 7 0c0 2-3.5 5.5-3.5 5.5z" fill="none" stroke="#333"/><circle cx="4.5" cy="4" r="1.2" fill="none" stroke="#333"/></svg>Germany, Hanover</div>
      <div class="meta time"><svg width="9" height="9" viewBox="0 0 9 9"><circle cx="4.5" cy="4.5" r="3.8" fill="none" stroke="#333"/><path d="M4.5 2.2v2.5l1.6 1" fill="none" stroke="#333"/></svg>65 days &nbsp;21:46:59</div>
      <div class="pay">$ 27500<span>Full Time</span></div>
      <div class="btn">View More</div>
    </div>
    <div class="job">
      <h3>ENGINEERING TECHNICIAN</h3>
      <div class="meta loc"><svg width="9" height="10" viewBox="0 0 9 10"><path d="M4.5 9.5S1 6 1 4a3.5 3.5 0 0 1 7 0c0 2-3.5 5.5-3.5 5.5z" fill="none" stroke="#333"/><circle cx="4.5" cy="4" r="1.2" fill="none" stroke="#333"/></svg>Germany, Hanover</div>
      <div class="meta time"><svg width="9" height="9" viewBox="0 0 9 9"><circle cx="4.5" cy="4.5" r="3.8" fill="none" stroke="#333"/><path d="M4.5 2.2v2.5l1.6 1" fill="none" stroke="#333"/></svg>65 days &nbsp;21:46:59</div>
      <div class="pay">$ 27500<span>Full Time</span></div>
      <div class="btn gold">View More</div>
    </div>
    <div class="job alt">
      <h3>SCIENCE TEACHER</h3>
      <div class="meta loc"><svg width="9" height="10" viewBox="0 0 9 10"><path d="M4.5 9.5S1 6 1 4a3.5 3.5 0 0 1 7 0c0 2-3.5 5.5-3.5 5.5z" fill="none" stroke="#333"/><circle cx="4.5" cy="4" r="1.2" fill="none" stroke="#333"/></svg>Germany, Hanover</div>
      <div class="meta time"><svg width="9" height="9" viewBox="0 0 9 9"><circle cx="4.5" cy="4.5" r="3.8" fill="none" stroke="#333"/><path d="M4.5 2.2v2.5l1.6 1" fill="none" stroke="#333"/></svg>65 days &nbsp;21:46:59</div>
      <div class="pay">$ 27500<span>Full Time</span></div>
      <div class="btn">View More</div>
    </div>
    <div class="job">
      <h3>ACCOUNTS ASSISTANT</h3>
      <div class="meta loc"><svg width="9" height="10" viewBox="0 0 9 10"><path d="M4.5 9.5S1 6 1 4a3.5 3.5 0 0 1 7 0c0 2-3.5 5.5-3.5 5.5z" fill="none" stroke="#333"/><circle cx="4.5" cy="4" r="1.2" fill="none" stroke="#333"/></svg>Germany, Hanover</div>
      <div class="meta time"><svg width="9" height="9" viewBox="0 0 9 9"><circle cx="4.5" cy="4.5" r="3.8" fill="none" stroke="#333"/><path d="M4.5 2.2v2.5l1.6 1" fill="none" stroke="#333"/></svg>65 days &nbsp;21:46:59</div>
      <div class="pay">$ 27500<span>Full Time</span></div>
      <div class="btn gold">View More</div>
    </div>
  </div>

  <article class="abs featured">
    <div class="photo" role="img" aria-label="Photo of a businessman in a suit on a city street">
      <div class="tag">$27500-$300000</div>
      <div class="role">Steak House Manager<br>Netherlands, Rotterdam</div>
    </div>
    <p class="text">Simply dummy text of the printing and type-setting industry. Lorem Ipsum has been the industry's standard dummy text ever since the 1500s when an unknown printer took a galley of type and scrambled it to make a type specimen book.</p>
    <p class="more">View More...</p>
  </article>
</section>

<footer class="abs footer">© Copyright 2017-Calder Ashby Recruitment &nbsp;| &nbsp;All Rights Reserved</footer>

</body>
</html>
```